Brackwell Immigration Law

We need a web design for our existing company www.brackwellcounsel.co.uk. We are an immigration consultancy. The final design should communicate professionalism, integrity and affordability.

Industry/Entity Type

It Company

Logo Text

Brackwell Counsel Partners

Number of Pages Required

5+ page

Font styles to use
Serif

Requirements
Must have
• I want to have the same silhouette logo but something different in positioning..
Nice to have
• Please have a look at these websites:
• https://www.travelpathguide.co.uk/visa_uk/
• http://www.oakdenadvisers.co.uk/
• http://www.myrtlegatelaw.org/index.php
• www.brackwellcounsel.co.uk

```html
<!DOCTYPE html>
<html lang="en">
<head>
<meta charset="utf-8">
<title>Brackwell Counsel Partners – UK Visa Services</title>
<link href="https://fonts.googleapis.com/css2?family=Droid+Serif&family=Open+Sans:wght@400;600;700&family=Roboto+Slab:wght@400;700&display=swap" rel="stylesheet">
<style>
:root{
  --gold:#f2a516;
  --gold-dark:#d98c00;
  --ink:#333;
  --muted:#777;
  --line:#e3e3e3;
  --band:#eeeeee;
  --dark:#1c1c1c;
  --white:#fff;
}
*{box-sizing:border-box;margin:0;padding:0}
html,body{width:781px;height:1200px;overflow:hidden;background:var(--white)}
body{font-family:"Open Sans",Arial,sans-serif;color:var(--ink);font-size:7px;line-height:1.45}

/* header */
.site-header{height:73px;display:flex;justify-content:space-between;align-items:flex-start;padding:12px 78px 0}
.brand{display:flex;align-items:center;gap:6px;margin-top:14px;font-family:"Roboto Slab",Georgia,serif;color:var(--gold-dark);font-size:15px;font-weight:700;line-height:1}
.brand-mark{width:10px;height:10px;background:var(--gold)}
.header-right{text-align:right}
.phone{display:inline-flex;align-items:center;gap:5px;font-size:13px;font-weight:600;color:#444}
.main-nav{display:flex;gap:2px;margin-top:10px}
.main-nav a{display:block;padding:5px 9px;font-size:6.5px;font-weight:600;color:#555;text-decoration:none;background:#f4f4f4}
.main-nav a.active{background:var(--gold);color:var(--white)}

/* hero */
.hero{position:relative;height:260px}
.hero-photo{position:absolute;inset:0;background:linear-gradient(180deg,#3d3a63 0%,#5a4f7a 40%,#2f3550 72%,#1c2233 100%)}
.hero-text{position:absolute;left:117px;top:96px;color:var(--white)}
.hero-text .kicker{font-family:"Droid Serif",Georgia,serif;font-size:12px;opacity:.9}
.hero-text h1{font-family:"Droid Serif",Georgia,serif;font-weight:400;font-size:32px;letter-spacing:.5px;line-height:1.15}
.assessment{position:absolute;left:494px;top:187px;width:196px;height:65px;background:var(--white);padding:8px 10px}
.assessment h3{font-family:"Roboto Slab",Georgia,serif;color:var(--gold-dark);font-size:9px}
.assessment p{font-size:5.5px;color:var(--muted)}
.assessment .select{margin-top:8px;width:80px;height:12px;border:1px solid #ccc;font-size:5px;color:#999;padding:2px 4px}

/* about */
.about{height:179px;padding:32px 78px 0}
.section-title{font-family:"Roboto Slab",Georgia,serif;font-size:10px;font-weight:700;color:var(--gold-dark);text-transform:uppercase;margin-bottom:10px}
.section-title span{color:#555}
.about p{font-size:5.5px;color:var(--muted);margin-bottom:6px}

/* services */
.services{position:relative;height:242px;padding:26px 78px 0}
.services::before{content:"";position:absolute;left:0;right:0;top:0;height:10px;background:var(--band)}
.arrow{position:absolute;top:118px;width:14px;height:14px}
.arrow.left{left:30px}.arrow.right{right:30px}
.visa-grid{display:grid;grid-template-columns:repeat(4,1fr);gap:4px 10px}
.visa-card{display:flex;height:100px}
.visa-photo{width:57px;height:100%;flex:none}
.visa-info{padding:8px 6px;flex:1}
.visa-info h4{font-family:"Roboto Slab",Georgia,serif;font-size:6.5px;color:var(--gold-dark);font-weight:700;line-height:1.2}
.visa-info h4 b{display:block;color:#444}
.visa-info p{font-size:5px;color:var(--muted);margin-top:4px}
.visa-info .more{display:block;margin-top:6px;font-size:5px;color:#444;font-weight:600}
.tone-a{background:linear-gradient(135deg,#c9a889,#6e5a4a)}
.tone-b{background:linear-gradient(135deg,#b8c4cf,#3d4a5a)}
.tone-c{background:linear-gradient(135deg,#d8b896,#8a6b56)}
.tone-d{background:linear-gradient(135deg,#e6c46a,#a77a3a)}

/* news + testimonials */
.lower{display:flex;gap:52px;height:143px;padding:20px 78px 0;border-top:1px solid var(--line)}
.news{width:260px}
.news-item{margin-bottom:8px}
.news-item .date{color:var(--gold-dark);font-size:5.5px;font-weight:700}
.news-item h5{font-size:6px;font-weight:700;color:#444}
.news-item p{font-size:5px;color:var(--muted)}
.news-item .more{font-size:5px;font-weight:600;color:#444}
.testimonials{flex:1}
.quote{border:1px solid var(--line);padding:8px 10px;position:relative;height:62px}
.quote .who{color:var(--gold-dark);font-size:6px;font-weight:700}
.quote p{font-size:5.5px;color:var(--muted);margin-top:3px}
.quote::after{content:"";position:absolute;left:20px;bottom:-6px;width:10px;height:10px;background:var(--white);border-right:1px solid var(--line);border-bottom:1px solid var(--line);transform:rotate(45deg)}
.quote-more{text-align:right;font-size:5px;color:#666;margin-top:6px}

/* contact */
.contact{height:221px;background:var(--dark);color:#ccc}
.contact h2{font-family:"Roboto Slab",Georgia,serif;color:var(--gold);font-weight:400;font-size:14px;text-align:center;padding-top:28px}
.contact h2::after{content:"";display:block;width:40px;height:1px;background:var(--gold);margin:4px auto 0}
.contact-body{display:flex;padding:16px 78px 0;gap:14px}
.map{width:130px;height:104px;flex:none;background:linear-gradient(135deg,#e2e2dc,#c6ccc4)}
.details{width:190px;font-size:5.5px;list-style:none}
.details li{display:flex;gap:6px;margin-bottom:8px;align-items:flex-start}
.details svg{flex:none}
.form{margin-left:auto;width:263px;display:grid;grid-template-columns:1fr 1fr;gap:6px}
.form label{font-size:5px;color:#aaa;display:block;margin-bottom:2px}
.field{height:14px;background:#2e2e2e;border:1px solid #3a3a3a}
.form .full{grid-column:1/3}
.field.tall{height:36px}
.btn{grid-column:1/3;height:18px;background:var(--gold);color:var(--white);font-weight:700;font-size:6.5px;display:flex;align-items:center;justify-content:center}

/* footer */
.site-footer{height:82px;padding:22px 78px 0;font-size:5px;color:var(--muted)}
.site-footer .reg{text-align:center}
.footer-row{display:flex;justify-content:space-between;align-items:center;margin-top:22px}
.socials{display:flex;gap:3px}
.socials span{width:8px;height:8px;background:var(--gold)}
</style>
</head>
<body>

<header class="site-header">
  <div class="brand"><span class="brand-mark"></span>Brackwell Counsel Partners</div>
  <div class="header-right">
    <div class="phone">
      <svg width="12" height="12" viewBox="0 0 24 24"><path fill="#d98c00" d="M6.6 10.8a15.1 15.1 0 0 0 6.6 6.6l2.2-2.2a1 1 0 0 1 1-.25 11.4 11.4 0 0 0 3.6.57 1 1 0 0 1 1 1V20a1 1 0 0 1-1 1A17 17 0 0 1 3 4a1 1 0 0 1 1-1h3.5a1 1 0 0 1 1 1c0 1.25.2 2.45.57 3.57a1 1 0 0 1-.25 1z"/></svg>
      0207 555 0143
    </div>
    <nav class="main-nav">
      <a class="active" href="#">HOME</a><a href="#">ABOUT US</a><a href="#">JOIN US</a><a href="#">NEWS</a><a href="#">BLOG</a><a href="#">CONTACT US</a>
    </nav>
  </div>
</header>

<section class="hero">
  <div class="hero-photo" role="img" aria-label="Photo of a city skyline at dusk"></div>
  <div class="hero-text">
    <div class="kicker">Brackwell Counsel Partners</div>
    <h1>UK VISA SERVICES</h1>
  </div>
  <div class="assessment">
    <h3>Visa Assessment</h3>
    <p>Brackwell Counsel Partners</p>
    <div class="select">Select Visa ▾</div>
  </div>
</section>

<section class="about">
  <h2 class="section-title">Brackwell <span>Counsel Partners</span></h2>
  <p>Brackwell Counsel Partners is regulated by the Immigration Advice Standards Board (IASB) and we have built our reputation on good quality legal work, delivered with care and a high percentage of positive outcomes.</p>
  <p>The majority of our clients come from personal recommendations as we are known for our up to date legal knowledge, attention to detail and clear advice.</p>
  <p>We are proud to be members of the Migration Practitioners Guild (MPG) and the Council for Migrant Welfare (CMW) in the United Kingdom.</p>
</section>

<section class="services">
  <svg class="arrow left" viewBox="0 0 14 14"><path d="M9 2 4 7l5 5" fill="none" stroke="#999" stroke-width="1.6"/></svg>
  <svg class="arrow right" viewBox="0 0 14 14"><path d="m5 2 5 5-5 5" fill="none" stroke="#999" stroke-width="1.6"/></svg>
  <div class="visa-grid">
    <article class="visa-card"><div class="visa-photo tone-a" role="img" aria-label="Photo of students"></div><div class="visa-info"><h4>STUDENT<b>VISAS</b></h4><p>Study routes for courses across the UK made simple.</p><span class="more">Read more »</span></div></article>
    <article class="visa-card"><div class="visa-photo tone-b" role="img" aria-label="Photo of business professionals"></div><div class="visa-info"><h4>WORK<b>VISAS</b></h4><p>Skilled worker routes for you and your employer.</p><span class="more">Read more »</span></div></article>
    <article class="visa-card"><div class="visa-photo tone-c" role="img" aria-label="Photo of a couple"></div><div class="visa-info"><h4>SPOUSE<b>VISAS</b></h4><p>Join your partner settled here in the UK.</p><span class="more">Read more »</span></div></article>
    <article class="visa-card"><div class="visa-photo tone-d" role="img" aria-label="Photo of travellers"></div><div class="visa-info"><h4>HOLIDAY<b>VISA</b></h4><p>Short visits for leisure and family time.</p><span class="more">Read more »</span></div></article>
    <article class="visa-card"><div class="visa-photo tone-c" role="img" aria-label="Photo of a family"></div><div class="visa-info"><h4>FAMILY<b>VISAS</b></h4><p>Bring loved ones together with clear advice.</p><span class="more">Read more »</span></div></article>
    <article class="visa-card"><div class="visa-photo tone-b" role="img" aria-label="Photo of tourists"></div><div class="visa-info"><h4>TOURIST<b>VISAS</b></h4><p>Visit the UK with a well prepared application.</p><span class="more">Read more »</span></div></article>
    <article class="visa-card"><div class="visa-photo tone-a" role="img" aria-label="Photo of a business meeting"></div><div class="visa-info"><h4>BUSINESS<b>VISAS</b></h4><p>Investor and founder routes for new ventures.</p><span class="more">Read more »</span></div></article>
    <article class="visa-card"><div class="visa-photo tone-d" role="img" aria-label="Photo of a group of friends"></div><div class="visa-info"><h4>SETTLEMENT<b>VISAS</b></h4><p>Indefinite leave and citizenship support.</p><span class="more">Read more »</span></div></article>
  </div>
</section>

<section class="lower">
  <div class="news">
    <h2 class="section-title"><span>Latest</span> News</h2>
    <div class="news-item"><div class="date">06.08.2015</div><h5>New Coverage Add</h5><p>Recent updates to the points based system explained.</p><span class="more">Read more »</span></div>
    <div class="news-item"><div class="date">06.08.2015</div><h5>New Coverage Add</h5><p>Changes to family route fees announced this month.</p><span class="more">Read more »</span></div>
  </div>
  <div class="testimonials">
    <h2 class="section-title">Client <span>Testimonials</span></h2>
    <div class="quote">
      <div class="who">Client Name</div>
      <p>The team guided us through every step of our application with patience and honesty. Their advice was clear, the fees were fair and our visa was granted without any delay. We would recommend them to anyone.</p>
    </div>
    <div class="quote-more">More testimonials »</div>
  </div>
</section>

<section class="contact">
  <h2>Contact Us</h2>
  <div class="contact-body">
    <div class="map" role="img" aria-label="Street map showing the office location"></div>
    <ul class="details">
      <li><svg width="8" height="10" viewBox="0 0 8 10"><path d="M4 0a3 3 0 0 0-3 3c0 2.3 3 7 3 7s3-4.7 3-7a3 3 0 0 0-3-3z" fill="#f2a516"/></svg><span>London Office, Brackwell House, 14 Fenmore Road, London E1 4QT. Two minutes from Fenmore Station.</span></li>
      <li><svg width="8" height="8" viewBox="0 0 24 24"><path fill="#f2a516" d="M6.6 10.8a15.1 15.1 0 0 0 6.6 6.6l2.2-2.2a1 1 0 0 1 1-.25 11.4 11.4 0 0 0 3.6.57 1 1 0 0 1 1 1V20a1 1 0 0 1-1 1A17 17 0 0 1 3 4a1 1 0 0 1 1-1h3.5a1 1 0 0 1 1 1c0 1.25.2 2.45.57 3.57a1 1 0 0 1-.25 1z"/></svg><span>0207 555 0143</span></li>
      <li><svg width="8" height="8" viewBox="0 0 8 8"><rect x="0.5" y="1.5" width="7" height="5" fill="none" stroke="#f2a516"/><path d="m.5 1.5 3.5 3 3.5-3" fill="none" stroke="#f2a516"/></svg><span>info@brackwellcounsel.co.uk</span></li>
      <li><svg width="8" height="8" viewBox="0 0 8 8"><circle cx="4" cy="4" r="3.5" fill="none" stroke="#f2a516"/><path d="M4 2v2h2" stroke="#f2a516" fill="none"/></svg><span>Mon – Fri, 9:00 – 18:00</span></li>
    </ul>
    <form class="form">
      <div><label>Your Name</label><div class="field"></div></div>
      <div><label>Email</label><div class="field"></div></div>
      <div class="full"><label>Message</label><div class="field tall"></div></div>
      <div class="btn">FIND OUT MORE</div>
    </form>
  </div>
</section>

<footer class="site-footer">
  <p class="reg">Regulated by the Immigration Advice Standards Board (IASB). Registered in England and Wales.</p>
  <div class="footer-row">
    <span>© 2015 Brackwell Counsel Partners. All Rights Reserved</span>
    <div class="socials"><span></span><span></span><span></span><span></span><span></span></div>
  </div>
</footer>

</body>
</html>
```